Business card

Looking for modern clean business card off logo below. Very important to be clean and professional but want fun as well

Industry/Entity Type

Business

```html
<!DOCTYPE html>
<html lang="en">
<head>
<meta charset="utf-8">
<title>Ridgeline Homes — Business Card</title>
<link href="https://fonts.googleapis.com/css2?family=Roboto+Condensed:wght@700&family=Lato:wght@400;700&display=swap" rel="stylesheet">
<style>
  :root {
    --stage: #d9d9d9;
    --teal: #1bb8d3;
    --teal-deep: #0fa3be;
    --teal-light: #5fd3e6;
    --white: #ffffff;
    --ink-gray: #6b6b6b;
    --charcoal: #3b3b3d;
    --charcoal-light: #4a4a4c;
    --paper-text: #f2f2f2;
  }
  * { box-sizing: border-box; margin: 0; padding: 0; }
  html, body {
    width: 1200px; height: 1000px; overflow: hidden;
    background: var(--stage);
  }
  .canvas {
    width: 1200px; height: 1000px;
    display: flex; flex-direction: column; align-items: center;
    justify-content: center; gap: 60px;
  }
  .card {
    width: 700px; height: 400px; position: relative; overflow: hidden;
    background: var(--white);
    box-shadow: 0 10px 28px rgba(0,0,0,0.25);
  }

  /* Brand lockup */
  .brand { display: flex; align-items: center; gap: 18px; }
  .brand-dot {
    flex: none; border-radius: 50%; background: var(--teal);
  }
  .brand-text { display: flex; flex-direction: column; }
  .brand-name {
    font-family: "Roboto Condensed", "Arial Narrow", sans-serif;
    font-weight: 700; color: var(--ink-gray); line-height: 1;
    letter-spacing: 0.5px; text-transform: uppercase;
  }
  .brand-tagline {
    font-family: "Lato", Arial, sans-serif; font-weight: 400;
    color: var(--ink-gray); line-height: 1.1;
  }

  /* Front */
  .front .band-top {
    position: absolute; left: 0; top: 0; width: 100%; height: 88px;
    background: linear-gradient(180deg, var(--teal) 0%, var(--teal-deep) 100%);
  }
  .front .band-middle {
    position: absolute; left: 0; top: 88px; width: 100%; height: 200px;
    background: var(--white);
    display: flex; align-items: center; justify-content: center;
  }
  .front .band-bottom {
    position: absolute; left: 0; top: 288px; width: 100%; height: 112px;
    background: linear-gradient(180deg, var(--teal-deep) 0%, var(--teal-light) 55%, var(--teal) 100%);
  }
  .front .brand-dot { width: 92px; height: 92px; }
  .front .brand-name { font-size: 64px; }
  .front .brand-tagline { font-size: 24px; margin-top: 4px; }

  /* Back */
  .back .band-logo {
    position: absolute; left: 0; top: 0; width: 100%; height: 128px;
    background: var(--white);
    display: flex; align-items: center; justify-content: flex-end;
    padding-right: 60px;
  }
  .back .brand-dot { width: 58px; height: 58px; }
  .back .brand-name { font-size: 42px; }
  .back .brand-tagline { font-size: 16px; margin-top: 3px; }
  .back .band-info {
    position: absolute; left: 0; top: 128px; width: 100%; height: 192px;
    background: linear-gradient(100deg, var(--charcoal) 0%, var(--charcoal-light) 45%, var(--charcoal) 100%);
  }
  .back .rule {
    position: absolute; left: 0; top: 320px; width: 100%; height: 8px;
    background: var(--white);
  }
  .back .band-bottom {
    position: absolute; left: 0; top: 328px; width: 100%; height: 72px;
    background: linear-gradient(180deg, var(--teal) 0%, var(--teal-light) 50%, var(--teal-deep) 100%);
  }
  .contact-list {
    list-style: none; position: absolute; left: 40px; top: 22px;
    font-family: "Lato", Arial, sans-serif; font-size: 17px;
    color: var(--paper-text); line-height: 1.25;
  }
  .contact-list li { display: flex; align-items: flex-start; gap: 14px; margin-bottom: 10px; }
  .contact-list svg { flex: none; width: 22px; height: 22px; margin-top: 3px; fill: var(--paper-text); }
  .person {
    position: absolute; right: 60px; bottom: 30px; text-align: right;
    font-family: "Lato", Arial, sans-serif; color: var(--paper-text);
  }
  .person-name { font-size: 24px; font-weight: 700; letter-spacing: 1px; text-transform: uppercase; }
  .person-title { font-size: 15px; margin-top: 2px; }
</style>
</head>
<body>
<main class="canvas">

  <section class="card front" aria-label="Card front">
    <div class="band-top"></div>
    <div class="band-middle">
      <div class="brand">
        <span class="brand-dot"></span>
        <div class="brand-text">
          <span class="brand-name">Ridgeline Homes</span>
          <span class="brand-tagline">Property Management and Real Estate</span>
        </div>
      </div>
    </div>
    <div class="band-bottom"></div>
  </section>

  <section class="card back" aria-label="Card back">
    <div class="band-logo">
      <div class="brand">
        <span class="brand-dot"></span>
        <div class="brand-text">
          <span class="brand-name">Ridgeline Homes</span>
          <span class="brand-tagline">Property Management and Real Estate</span>
        </div>
      </div>
    </div>
    <div class="band-info">
      <ul class="contact-list">
        <li>
          <svg viewBox="0 0 24 24" aria-hidden="true"><path d="M6.6 10.8a15.1 15.1 0 0 0 6.6 6.6l2.2-2.2a1 1 0 0 1 1-.25 11.4 11.4 0 0 0 3.6.57 1 1 0 0 1 1 1V20a1 1 0 0 1-1 1A17 17 0 0 1 3 4a1 1 0 0 1 1-1h3.5a1 1 0 0 1 1 1c0 1.25.2 2.45.57 3.57a1 1 0 0 1-.25 1z"/></svg>
          <span>+000 - 2468 - 1357<br>+000 - 8642 - 9753</span>
        </li>
        <li>
          <svg viewBox="0 0 24 24" aria-hidden="true"><path d="M12 2a10 10 0 1 0 0 20 10 10 0 0 0 0-20zm6.9 6h-2.9a15.7 15.7 0 0 0-1.4-3.6A8 8 0 0 1 18.9 8zM12 4c.8 1.2 1.5 2.5 1.9 4h-3.8c.4-1.5 1.1-2.8 1.9-4zM4.3 14a8 8 0 0 1 0-4h3.4a16 16 0 0 0 0 4zm.8 2h2.9c.3 1.3.8 2.5 1.4 3.6A8 8 0 0 1 5.1 16zM8 8H5.1a8 8 0 0 1 4.3-3.6C8.8 5.5 8.4 6.7 8 8zm4 12c-.8-1.2-1.5-2.5-1.9-4h3.8c-.4 1.5-1.1 2.8-1.9 4zm2.3-6H9.7a14.7 14.7 0 0 1 0-4h4.6a14.7 14.7 0 0 1 0 4zm.3 5.6c.6-1.1 1.1-2.3 1.4-3.6h2.9a8 8 0 0 1-4.3 3.6zm1.7-5.6a16 16 0 0 0 0-4h3.4a8 8 0 0 1 0 4z"/></svg>
          <span>dana.reyes@ridgelinehomes.com<br>ridgelinehomes.com</span>
        </li>
        <li>
          <svg viewBox="0 0 24 24" aria-hidden="true"><path d="M12 3 2 12h3v8h5v-5h4v5h5v-8h3z"/></svg>
          <span>410 Harbor Lane,<br>Brookfield 24680</span>
        </li>
      </ul>
      <div class="person">
        <div class="person-name">Dana Reyes</div>
        <div class="person-title">Director</div>
      </div>
    </div>
    <div class="rule"></div>
    <div class="band-bottom"></div>
  </section>

</main>
</body>
</html>
```